RW Frameworks Inc Business cards

We need business cards using our existing logo but slightly modified. Right now the logo says RW Framework Masonry. We want to keep the RW part of the design, but replace the Framework Masonry portion with "FRAMEWORKS". Please see the attached file.
Ideally this would be a blank template so we can add Different Names, titles, and phone numbers later.
On the one side we want only the logo and on the other side the detail. I'm attaching an example for you to see.
Please reach out with any other questions. Our address and other details will be given out once we find a design we like.

Target Market(s)

Construction Industry

```html
<!DOCTYPE html>
<html lang="en">
<head>
<meta charset="UTF-8">
<title>RW Frameworks Inc – Business Cards</title>
<link href="https://fonts.googleapis.com/css2?family=Roboto:wght@300;400;700&display=swap" rel="stylesheet">
<style>
  :root {
    --page-bg: #e9e7e3;
    --card-white: #f7f7f7;
    --brand-blue: #2f7fc6;
    --brand-grey: #8f9295;
    --text-grey: #6d7074;
    --rule-grey: #9a9da0;
    --white: #ffffff;
  }
  * { margin: 0; padding: 0; box-sizing: border-box; }
  html, body {
    width: 900px; height: 1200px; overflow: hidden;
    background: var(--page-bg);
    font-family: "Roboto", sans-serif;
  }
  .canvas { position: relative; width: 900px; height: 1200px; }
  .card {
    position: absolute; left: 60px; width: 780px; height: 445px;
    border-radius: 24px; overflow: hidden;
    box-shadow: 0 6px 18px rgba(0,0,0,0.18);
  }
  .card--front { top: 120px; background: var(--card-white); }
  .card--back { top: 640px; background: var(--brand-blue); }
  .card__shapes { position: absolute; inset: 0; width: 100%; height: 100%; }

  .logo { position: absolute; text-align: center; font-weight: 700; line-height: 1; }
  .logo__mark { display: block; font-size: 80px; letter-spacing: 2px; }
  .logo__name { display: block; font-size: 19px; letter-spacing: 5px; margin-top: 8px; }
  .card--front .logo { left: 40px; top: 170px; width: 225px; color: var(--brand-blue); }
  .card--back .logo { left: 0; right: 0; top: 160px; color: var(--white); }
  .card--back .logo__mark { font-size: 96px; }
  .card--back .logo__name { font-size: 22px; letter-spacing: 6px; }

  .divider {
    position: absolute; left: 292px; top: 170px; width: 2px; height: 110px;
    background: var(--rule-grey);
  }
  .details { position: absolute; left: 322px; top: 180px; }
  .details__name {
    font-size: 27px; font-weight: 700; color: var(--brand-blue);
    text-transform: uppercase; letter-spacing: 1px;
  }
  .details__title {
    font-size: 13px; font-weight: 400; color: var(--text-grey);
    text-transform: uppercase; letter-spacing: 1px; margin-top: 4px;
  }
  .details__list { list-style: none; margin-top: 20px; }
  .details__item {
    display: flex; align-items: center; gap: 10px;
    font-size: 16px; font-weight: 300; color: var(--text-grey); margin-bottom: 9px;
  }
  .details__icon {
    width: 20px; height: 20px; border-radius: 3px; background: var(--brand-blue);
    display: flex; align-items: center; justify-content: center;
  }
</style>
</head>
<body>
<main class="canvas">

  <section class="card card--front" aria-label="Business card, detail side">
    <svg class="card__shapes" viewBox="0 0 780 445" preserveAspectRatio="none" aria-hidden="true">
      <path d="M0,0 H780 V170 C720,165 660,120 600,80 C520,35 420,55 300,58 C180,60 80,45 0,38 Z" fill="var(--brand-blue)"/>
      <path d="M0,48 C80,55 180,70 300,68 C420,65 520,48 595,92 C655,130 715,178 780,182" fill="none" stroke="var(--white)" stroke-width="6"/>
      <path d="M780,255 C690,262 620,300 560,360 C520,400 480,430 440,445 H780 Z" fill="var(--brand-grey)"/>
    </svg>

    <div class="logo">
      <span class="logo__mark">RW</span>
      <span class="logo__name">FRAMEWORKS</span>
    </div>

    <div class="divider"></div>

    <div class="details">
      <p class="details__name">Daniel Hart</p>
      <p class="details__title">Project Manager</p>
      <ul class="details__list">
        <li class="details__item">
          <span class="details__icon">
            <svg width="12" height="12" viewBox="0 0 24 24" aria-hidden="true"><path fill="#fff" d="M6.6 10.8a15.1 15.1 0 0 0 6.6 6.6l2.2-2.2a1 1 0 0 1 1-.25 11.4 11.4 0 0 0 3.6.57 1 1 0 0 1 1 1V20a1 1 0 0 1-1 1A17 17 0 0 1 3 4a1 1 0 0 1 1-1h3.5a1 1 0 0 1 1 1c0 1.25.2 2.45.57 3.57a1 1 0 0 1-.25 1z"/></svg>
          </span>
          (03) 95550142
        </li>
        <li class="details__item">
          <span class="details__icon">
            <svg width="12" height="12" viewBox="0 0 24 24" aria-hidden="true"><path fill="#fff" d="M2 5h20v14H2z M2 5l10 8 10-8" stroke="#2f7fc6" stroke-width="1.6"/></svg>
          </span>
          daniel@rwframeworks.com
        </li>
      </ul>
    </div>
  </section>

  <section class="card card--back" aria-label="Business card, logo side">
    <svg class="card__shapes" viewBox="0 0 780 445" preserveAspectRatio="none" aria-hidden="true">
      <path d="M0,0 H780 V40 C660,45 560,60 470,100 C380,140 250,130 150,110 C90,98 40,100 0,108 Z" fill="var(--brand-grey)"/>
      <path d="M0,118 C40,110 90,108 150,120 C250,140 380,150 470,110 C560,70 660,55 780,50" fill="none" stroke="var(--white)" stroke-width="6"/>
      <path d="M0,330 C60,345 120,380 170,445 H0 Z" fill="var(--brand-grey)"/>
    </svg>

    <div class="logo">
      <span class="logo__mark">RW</span>
      <span class="logo__name">FRAMEWORKS</span>
    </div>
  </section>

</main>
</body>
</html>
```